New (old) Business Card Design Project

I would like to purchase a customized version of a design you have previously submitted - https://www.artboardhub.example/design/7305816

I like the card above, and would like to use the same design, jus with my business name, CARRINGFORD ASSET ADVISORY. I like the colors in the card above, as well as the font. The other side will have my name, company name, address, phone, email, website, plus disclosure text I will provide.

Target Market(s)

wealthy families

Industry/Entity Type

Financial Services

Contact Information for Business Card

logo on one side, on other my name, company, address, phone, email, website, disclosure language I will provide.

Colors

Designer to choose colors to be used in the design.

Requirements
Must have
• colors: Deep blue and white
Nice to have
• Please see the items I have uploaded, below.
Should not have
• Cheap, tacky look.

```html
<!DOCTYPE html>
<html lang="en">
<head>
<meta charset="utf-8">
<title>Carringford Asset Advisory — Business Card</title>
<link rel="stylesheet" href="https://fonts.googleapis.com/css2?family=Arimo:wght@400&family=Libre+Caslon+Text:ital,wght@0,400;1,700&display=swap">
<style>
  :root {
    --navy: #0d1f63;
    --white: #ffffff;
    --rule: rgba(255, 255, 255, 0.7);
    --backdrop: #e6e5e2;
  }
  * { margin: 0; padding: 0; box-sizing: border-box; }
  html, body {
    width: 1200px;
    height: 801px;
    overflow: hidden;
    background: var(--backdrop);
  }
  .canvas {
    position: relative;
    width: 1200px;
    height: 801px;
  }
  .card {
    position: absolute;
    top: 246px;
    width: 540px;
    height: 309px;
    background: var(--navy);
    color: var(--white);
  }
  .card--contact { left: 40px; }
  .card--brand { left: 620px; }

  /* Contact side */
  .contact-brand {
    position: absolute;
    left: 34px;
    bottom: 62px;
    font-family: "Libre Caslon Text", serif;
    font-weight: 400;
    font-size: 16px;
    letter-spacing: 2px;
    line-height: 1.35;
    white-space: nowrap;
  }
  .contact-divider {
    position: absolute;
    left: 262px;
    top: 40px;
    width: 1px;
    height: 200px;
    background: var(--rule);
  }
  .contact-details {
    position: absolute;
    left: 290px;
    top: 40px;
    font-family: "Arimo", sans-serif;
    font-size: 13px;
    line-height: 1.3;
    white-space: nowrap;
  }
  .person-name {
    font-family: "Libre Caslon Text", serif;
    font-size: 19px;
    letter-spacing: 1.5px;
    line-height: 1.1;
  }
  .person-role { margin-bottom: 14px; }
  .address { margin-bottom: 14px; }
  .contact-line {
    display: flex;
    align-items: center;
    gap: 8px;
    margin-bottom: 2px;
  }
  .contact-line svg { width: 12px; height: 12px; flex: none; }

  /* Brand side */
  .brand-name {
    position: absolute;
    left: 0;
    right: 0;
    top: 112px;
    text-align: center;
    font-family: "Libre Caslon Text", serif;
    font-weight: 400;
    font-size: 21px;
    letter-spacing: 2.5px;
    white-space: nowrap;
  }
  .tagline {
    position: absolute;
    left: 70px;
    right: 70px;
    top: 196px;
    display: flex;
    justify-content: space-between;
    font-family: "Libre Caslon Text", serif;
    font-style: italic;
    font-weight: 700;
    font-size: 18px;
    letter-spacing: 0.5px;
  }
</style>
</head>
<body>
<main class="canvas">

  <section class="card card--contact" aria-label="Business card, contact side">
    <div class="contact-brand">CARRINGFORD<br>ASSET ADVISORY</div>
    <div class="contact-divider"></div>
    <div class="contact-details">
      <div class="person-name">EVERETT HALE</div>
      <div class="person-role">Manager</div>
      <div class="address">Your address, city<br>state, ZIP 0000</div>
      <div class="contact-line">
        <svg viewBox="0 0 12 12" aria-hidden="true"><path fill="#fff" d="M2.5 1 4.3 3.2 3.4 4.4c.6 1.5 1.7 2.6 3.2 3.2l1.2-.9L10 8.5 9 10.6C5 10.6 1.4 7 1.4 3Z"/></svg>
        <span>555-013-4826</span>
      </div>
      <div class="contact-line">
        <svg viewBox="0 0 12 12" aria-hidden="true"><rect x="1" y="2.5" width="10" height="7" fill="#fff"/><path d="M1 2.5 6 6.5 11 2.5" fill="none" stroke="#0d1f63" stroke-width="1"/></svg>
        <span>youremail@mailbox.example</span>
      </div>
      <div class="contact-line">
        <svg viewBox="0 0 12 12" aria-hidden="true"><circle cx="6" cy="6" r="5" fill="#fff"/><path d="M1 6h10M6 1c-2 2.6-2 7.4 0 10M6 1c2 2.6 2 7.4 0 10" fill="none" stroke="#0d1f63" stroke-width="0.9"/></svg>
        <span>www.yourwebsite.example</span>
      </div>
    </div>
  </section>

  <section class="card card--brand" aria-label="Business card, brand side">
    <div class="brand-name">CARRINGFORD ASSET ADVISORY</div>
    <div class="tagline">
      <span>Grow</span>
      <span>Protect</span>
      <span>Endow</span>
    </div>
  </section>

</main>
</body>
</html>
```